Hello again

I have a few Logos I am looking to add

Target Market(s)

MediSpa

Industry/Entity Type

Medispa

Contact Information for Business Card

Dana Whitcombe, Owner/Medical Aesthetician, 403-812-3957, Unit 148 - 1920 5 st NW, T3K 1M7 Calgary, AB., www.LarkMediSpa.ca ....QR codes are attached I do really like the former business card but everything was in teal, gold and white.

```html
<!DOCTYPE html>
<html lang="en">
<head>
<meta charset="utf-8">
<title>Lark MediSpa – Business Card</title>
<link href="https://fonts.googleapis.com/css2?family=Libre+Baskerville&family=Arimo&display=swap" rel="stylesheet">
<style>
  :root {
    --page-bg: #3d3d3d;
    --card-bg: #2e2e2e;
    --gold: #c9a956;
    --white: #f4f4f4;
    --divider: #8a8a8a;
  }
  * { margin: 0; padding: 0; box-sizing: border-box; }
  html, body { width: 1200px; height: 1200px; overflow: hidden; }
  body { background: var(--page-bg); position: relative; font-family: "Arimo", Arial, sans-serif; }

  .card {
    position: absolute;
    width: 686px;
    height: 393px;
    border-radius: 26px;
    background: var(--card-bg);
  }
  .card--front { left: 267px; top: 158px; }
  .card--back  { left: 263px; top: 652px; }

  .brand {
    position: absolute;
    display: flex;
    align-items: center;
    font-family: "Libre Baskerville", Georgia, serif;
    font-weight: 400;
    color: var(--gold);
    white-space: nowrap;
  }
  .brand__dot { border-radius: 50%; background: var(--gold); flex: none; }

  .card--front .brand { left: 80px; top: 170px; font-size: 34px; gap: 12px; }
  .card--front .brand__dot { width: 14px; height: 14px; }

  .card--back .brand { left: 0; right: 0; top: 160px; justify-content: center; font-size: 62px; gap: 20px; }
  .card--back .brand__dot { width: 24px; height: 24px; }

  .divider {
    position: absolute;
    left: 374px; top: 109px;
    width: 1px; height: 168px;
    background: linear-gradient(to bottom, transparent, var(--divider) 20%, var(--divider) 80%, transparent);
  }

  .contact { position: absolute; left: 405px; top: 108px; color: var(--white); }
  .contact__name {
    font-family: "Libre Baskerville", Georgia, serif;
    font-weight: 400;
    font-size: 25px;
    color: var(--gold);
    line-height: 1.2;
  }
  .contact__role { font-size: 15.5px; margin-top: 1px; }
  .contact__address { font-size: 16px; line-height: 21px; margin-top: 22px; }
  .contact__list { list-style: none; margin-top: 12px; font-size: 16px; }
  .contact__item { display: flex; align-items: center; gap: 10px; height: 21px; }
  .contact__icon { width: 15px; height: 15px; flex: none; fill: var(--gold); }
</style>
</head>
<body>
  <section class="card card--front">
    <div class="brand"><span class="brand__dot"></span>Lark MediSpa</div>
    <div class="divider"></div>
    <div class="contact">
      <h1 class="contact__name">Dana Whitcombe</h1>
      <p class="contact__role">Owner/Medical Aesthetician</p>
      <p class="contact__address">Unit 148 - 1920 5 st NW<br>Calgary, AB, T3K 1M7</p>
      <ul class="contact__list">
        <li class="contact__item">
          <svg class="contact__icon" viewBox="0 0 24 24" aria-hidden="true"><path d="M6.6 10.8a15.1 15.1 0 0 0 6.6 6.6l2.2-2.2c.3-.3.7-.4 1-.2 1.1.4 2.3.6 3.6.6.6 0 1 .4 1 1V20c0 .6-.4 1-1 1A17 17 0 0 1 3 4c0-.6.4-1 1-1h3.5c.6 0 1 .4 1 1 0 1.3.2 2.5.6 3.6.1.3 0 .7-.2 1z"/></svg>
          <span>403-812-3957</span>
        </li>
        <li class="contact__item">
          <svg class="contact__icon" viewBox="0 0 24 24" aria-hidden="true"><circle cx="12" cy="12" r="10"/><path d="M8 5c2 1 1 3 3 4s1 3-1 3-3 2-2 4M15 14c1 0 2 1 2 3M16 6c-1 1 0 2 1 2" stroke="#2e2e2e" stroke-width="1.6" fill="none"/></svg>
          <span>www.LarkMediSpa.ca</span>
        </li>
      </ul>
    </div>
  </section>

  <section class="card card--back">
    <div class="brand"><span class="brand__dot"></span>Lark MediSpa</div>
  </section>
</body>
</html>
```